quorvadeal.com redesign with wireframes, white space and custom form are very important

Need a new two column design that will convert easily to mobile responsive. Lots of white space. Winning design will probably be based on header area and making the custom form stand out. I want the header to be very much like www.talbekmo.com except the form not to go up into the header.
Here are some of the websites I really like:
www.pivrostacks.com
http://glendarokfastmove.com/
http://morquilandestate.com/

We buy homes for cash and close fast. Our target is a home seller who is desperate to sell quickly.
I have uploaded my really ugly wireframe and my logo. I also uploaded my photo for the about us box and a possible photo to use for the header.
The copy on the wireframe is what I will be using except for the about us box.

Here is the exact link for video to frame in the top left box.
https://example-vidhost.net/Kp39xqTzR2a

Number of Pages Required

1 page

Font styles to use
Sans Serif

Colors
0592cd
85cae6
eaf1f7
fbee3d
ec1f27

Requirements
Must have
• Everything on wireframe.
• Must use Verdana font and nothing should be smaller than 12 point. Most should be in 14 point. (except maybe inside of form)

```html
<!DOCTYPE html>
<html lang="en">
<head>
<meta charset="utf-8">
<title>quorvadeal.com – Sell Your Home For Cash</title>
<link rel="stylesheet" href="https://fonts.googleapis.com/css2?family=Open+Sans:ital,wght@0,400;0,600;0,700;0,800;1,400;1,700&display=swap">
<style>
:root{
  --red:#e31e24;
  --blue:#0592cd;
  --light-blue:#85cae6;
  --pale:#eaf1f7;
  --ink:#1d1d1d;
  --text:#444;
  --muted:#9a9a9a;
  --field-line:#d9e2ea;
  --soft-gray:#f4f4f4;
  --side-gray:#efefef;
  --footer:#222;
}
*{box-sizing:border-box;margin:0;padding:0}
html,body{width:1200px;height:3018px;overflow:hidden}
body{font-family:"Open Sans",sans-serif;color:var(--text);background:#fff;position:relative;font-size:14px}
.abs{position:absolute}
ul{list-style:none}

/* header */
.brand{left:88px;top:52px;display:flex;align-items:center;gap:7px;font-size:17px;font-weight:800;color:var(--red)}
.brand-square{width:14px;height:14px;background:var(--red)}
.main-nav{left:270px;top:63px;display:flex;align-items:center;gap:28px;font-size:12.5px;font-weight:700;color:#777;letter-spacing:.3px}
.call-box{right:88px;top:30px;text-align:right}
.call-box .label{color:var(--red);font-weight:800;font-size:19px}
.call-box .hours{font-size:11px;font-weight:600;color:#555}
.call-box .phone{color:var(--red);font-weight:800;font-size:25px;line-height:1.2}

/* hero */
.hero-photo{left:88px;top:134px;width:1024px;height:309px;background:linear-gradient(180deg,#d4e2f0 0%,#aebfd1 22%,#8a96a3 42%,#6b737c 60%,#7c8464 80%,#46552f 100%)}
.hero-title{left:88px;top:206px;width:1024px;text-align:center;color:#fff;font-weight:800;text-shadow:0 2px 5px rgba(0,0,0,.45)}
.hero-title .line1{font-size:37px;letter-spacing:.5px}
.hero-title .line2{font-size:54px;line-height:1.1}
.hero-band{left:76px;top:369px;width:1048px;height:51px;background:var(--red);color:#fff;text-align:center;font-size:27px;line-height:51px;letter-spacing:.5px;box-shadow:0 3px 6px rgba(0,0,0,.25)}

/* benefits */
.benefits-title{left:88px;top:484px;font-size:22px;font-weight:800;color:var(--ink);line-height:1.2}
.benefits-title em{font-style:normal;color:var(--red)}
.benefits-list{left:88px;top:556px;font-size:13.5px;font-weight:700;font-style:italic;color:var(--ink)}
.benefits-list li{display:flex;align-items:center;gap:10px;height:22px;margin-bottom:5px}
.benefits-list .hl{color:var(--red)}
.curve-arrow{left:460px;top:510px}
.video-label{left:88px;top:670px;font-size:18px;font-weight:800;color:var(--ink);line-height:1.25}
.video-frame{left:88px;top:734px;width:512px;height:309px;background:#151515}
.video-bar{height:32px;background:#2a2a2a;display:flex;align-items:center;justify-content:space-between;padding:0 14px}
.video-bar .tag{width:52px;height:14px;background:#555}

/* lead form */
.lead-form{left:625px;top:489px;width:467px;height:554px;background:var(--pale);border-radius:4px}
.form-tab{position:absolute;left:26px;top:0;width:46px;height:24px;background:var(--red);border-radius:0 0 23px 23px}
.form-title{position:absolute;left:0;top:38px;width:100%;text-align:center;font-size:21px;font-weight:800;color:var(--blue)}
.form-title em{font-style:normal;color:var(--red)}
.form-sub{position:absolute;left:0;top:72px;width:100%;text-align:center;font-size:13px;color:#555}
.field{position:absolute;background:#fff;border:1px solid var(--field-line);font-size:12px;color:#aab;padding:10px 12px}
.submit-btn{position:absolute;left:24px;top:448px;width:418px;height:48px;background:var(--red);border-radius:3px;color:#fff;font-size:14px;font-weight:700;text-align:center;line-height:48px}
.privacy-note{position:absolute;right:26px;top:520px;font-size:12px;color:#aab;display:flex;align-items:center;gap:6px}

/* sell section */
.sell-band{left:0;top:1089px;width:1200px;height:583px;background:var(--soft-gray)}
.sell-title{left:88px;top:1148px;width:500px;font-size:22px;font-weight:800;color:var(--ink);line-height:1.25}
.sell-copy{left:88px;top:1262px;width:510px;font-size:14px;line-height:1.55;color:#444}
.sell-copy strong{color:var(--red)}
.reasons-title{left:88px;top:1378px;font-size:18px;font-weight:800;color:var(--ink)}
.reasons-list{left:88px;top:1419px;font-size:13.5px;font-weight:700;font-style:italic;color:var(--ink)}
.reasons-list li{display:flex;align-items:center;gap:10px;height:23px}
.help-line{left:88px;top:1576px;width:500px;font-size:19px;color:var(--blue);line-height:1.3}

.privacy-btn{left:669px;top:1154px;width:200px;height:48px;background:var(--red);border-radius:3px;color:#fff;font-size:13px;font-weight:700;text-align:center;line-height:48px}
.share-squares{left:880px;top:1154px;display:flex;gap:8px}
.share-squares span{width:48px;height:48px;border-radius:3px;background:#cfcfcf;box-shadow:inset 0 -3px 0 rgba(0,0,0,.08)}
.share-squares span.mid{background:#3b5b98}
.call-hours{left:625px;top:1232px;width:467px;text-align:center;font-size:19px;font-weight:800;color:var(--ink);line-height:1.3}
.call-hours em{font-style:normal;color:var(--red)}
.testimonials-title{left:625px;top:1350px;width:467px;text-align:center;font-size:18px;font-weight:800;color:var(--red)}
.testimonial-quote{left:628px;top:1392px;width:462px;text-align:center;font-size:13.5px;line-height:1.6}
.testimonial-name{left:625px;top:1454px;width:467px;text-align:center;font-size:13.5px;font-weight:700;color:var(--ink)}
.dots{left:836px;top:1508px;display:flex;gap:6px}
.dots span{width:9px;height:9px;border-radius:50%;background:#ccc}
.dots span.on{background:#fff;border:2px solid var(--red)}
.more-btn{left:722px;top:1548px;width:270px;height:47px;background:#d6d6d6;color:#fff;font-size:13px;font-weight:700;text-align:center;line-height:47px;border-radius:3px}

/* blog + sidebar */
.sidebar-bg{left:614px;top:1672px;width:586px;height:1188px;background:var(--side-gray)}
.post-photo{position:absolute;left:88px;width:507px;height:148px;background:linear-gradient(180deg,#b7cde3 0%,#d9e4ee 22%,#f2f0ea 40%,#d8d4ca 58%,#5f7436 78%,#3f5224 100%)}
.post-title{position:absolute;left:88px;font-size:18px;font-weight:800;color:var(--ink)}
.post-title.active{color:var(--red)}
.post-meta{position:absolute;left:300px;font-size:12px;color:var(--muted);display:flex;gap:26px}
.post-meta span{display:flex;align-items:center;gap:7px}
.post-text{position:absolute;left:88px;width:512px;font-size:13.5px;line-height:1.5;color:#444}
.post-text i{color:var(--muted);font-weight:700;margin-left:4px}
.post-text i.active{color:var(--red)}
.archive-list{left:88px;top:2680px;font-size:13.5px;font-weight:700;font-style:italic;color:var(--ink)}
.archive-list li{display:flex;align-items:center;gap:12px;height:22px}
.archive-list li::before{content:"";width:7px;height:7px;border-radius:50%;background:var(--ink)}

.about-photo{left:628px;top:1728px;width:115px;height:104px;background:linear-gradient(180deg,#6f8c4a 0%,#93ab6c 55%,#b9c59a 100%)}
.about-title{left:757px;top:1746px;font-size:18px;font-weight:800;color:var(--red)}
.about-copy{left:757px;top:1778px;width:335px;font-size:13px;line-height:1.55}
.rule{height:1px;background:#dcdcdc;width:466px;left:625px}
.cities-title{left:625px;top:1928px;width:466px;font-size:18px;font-weight:800;color:var(--red);line-height:1.3}
.cities-lead{left:625px;top:2002px;width:466px;font-size:13px;font-weight:700;color:var(--ink);line-height:1.5}
.cities-copy{left:625px;top:2046px;width:466px;font-size:13px;line-height:1.5}
.cities-copy strong{color:var(--red)}
.types-lead{left:625px;top:2230px;font-size:13px;font-weight:700;color:var(--ink)}
.types-copy{left:625px;top:2256px;width:466px;font-size:13px;line-height:1.5}
.houses-photo{top:2358px;height:176px;width:232px}
.houses-photo.left{left:625px;background:linear-gradient(180deg,#c6d4e4 0%,#b6c0c8 30%,#7d8a6c 55%,#3f5a26 80%,#9b9c94 100%)}
.houses-photo.right{left:859px;background:linear-gradient(180deg,#9db9d8 0%,#d5dbe0 35%,#8f8a80 55%,#4f6b2c 75%,#6d8a3c 100%)}
.houses-caption{left:625px;top:2552px;width:466px;font-size:18px;font-weight:800;color:var(--red);line-height:1.3}

/* footer */
.site-footer{left:0;top:2860px;width:1200px;height:158px;background:var(--footer)}
.footer-nav{position:absolute;left:0;top:58px;width:100%;display:flex;justify-content:center;gap:28px;font-size:12px;font-weight:700;color:#aaa;letter-spacing:.3px}
.copyright{position:absolute;left:0;top:90px;width:100%;text-align:center;font-size:11px;color:#777}
</style>
</head>
<body>

<header>
  <div class="abs brand"><span class="brand-square"></span>quorvadeal.com</div>
  <nav class="abs main-nav">
    <span>SELL YOUR HOME</span><span>HOW IT WORKS</span><span>STOP FORECLOSURE</span><span>PROBATE</span><span>CONTACT</span>
    <svg width="13" height="13" viewBox="0 0 13 13"><circle cx="5.5" cy="5.5" r="4" fill="none" stroke="#777" stroke-width="1.6"/><line x1="8.5" y1="8.5" x2="12" y2="12" stroke="#777" stroke-width="1.6"/></svg>
  </nav>
  <div class="abs call-box">
    <div class="label">CALL US</div>
    <div class="hours">Nights and weekends ok</div>
    <div class="phone">407-555-0193</div>
  </div>
</header>

<section>
  <div class="abs hero-photo" role="img" aria-label="Photo of a suburban street lined with two-storey houses under a blue sky"></div>
  <h1 class="abs hero-title"><div class="line1">SELL YOUR HOME FOR CASH IN</div><div class="line2">8 DAYS</div></h1>
  <div class="abs hero-band">WE BUY HOUSES NATIONWIDE</div>
</section>

<section>
  <h2 class="abs benefits-title">THESE ARE THE BENEFITS OF <em>SELLING</em><br>YOUR HOME TO US.</h2>
  <svg class="abs curve-arrow" width="150" height="60" viewBox="0 0 150 60"><path d="M5 8 C40 10 70 60 140 44" fill="none" stroke="var(--red)" stroke-width="3"/><path d="M128 34 L142 44 L128 54" fill="none" stroke="var(--red)" stroke-width="3"/></svg>
  <ul class="abs benefits-list">
    <li><svg width="14" height="14" viewBox="0 0 14 14"><circle cx="7" cy="7" r="6" fill="none" stroke="var(--red)" stroke-width="1.5"/><path d="M4 7 L6.3 9.3 L10.5 4.5" fill="none" stroke="var(--red)" stroke-width="1.7"/></svg><span>You Pick The <span class="hl">Closing Date</span></span></li>
    <li><svg width="14" height="14" viewBox="0 0 14 14"><circle cx="7" cy="7" r="6" fill="none" stroke="var(--red)" stroke-width="1.5"/><path d="M4 7 L6.3 9.3 L10.5 4.5" fill="none" stroke="var(--red)" stroke-width="1.7"/></svg><span>You Pay <span class="hl">NO</span> Commissions Or Fees</span></li>
    <li><svg width="14" height="14" viewBox="0 0 14 14"><circle cx="7" cy="7" r="6" fill="none" stroke="var(--red)" stroke-width="1.5"/><path d="M4 7 L6.3 9.3 L10.5 4.5" fill="none" stroke="var(--red)" stroke-width="1.7"/></svg><span>You <span class="hl">Don't</span> Have To Paint, Clean Or Make Repairs</span></li>
  </ul>
  <h3 class="abs video-label">Watch to see our president Marlon explain how<br>easy it is to sell to us.</h3>
  <div class="abs video-frame" role="img" aria-label="Embedded video player">
    <div class="video-bar"><span class="tag"></span>
      <svg width="40" height="14" viewBox="0 0 40 14"><g fill="#999"><rect x="0" y="1" width="3" height="3"/><rect x="5" y="1" width="3" height="3"/><rect x="0" y="6" width="3" height="3"/><rect x="5" y="6" width="3" height="3"/></g><circle cx="30" cy="6" r="4" fill="none" stroke="#999" stroke-width="1.5"/><line x1="33" y1="9" x2="36" y2="12" stroke="#999" stroke-width="1.5"/></svg>
    </div>
  </div>

  <form class="abs lead-form">
    <span class="form-tab"></span>
    <h2 class="form-title"><em>YES,</em> I WANT TO SELL MY HOME FAST!</h2>
    <p class="form-sub">Get a no obligation written offer in 36 hours</p>
    <div class="field" style="left:24px;top:102px;width:204px;height:42px">Your Name*</div>
    <div class="field" style="left:236px;top:102px;width:206px;height:42px">Your phone number*</div>
    <div class="field" style="left:24px;top:148px;width:204px;height:42px">Your Email Address*</div>
    <div class="field" style="left:236px;top:148px;width:206px;height:42px">Asking price*</div>
    <div class="field" style="left:24px;top:194px;width:418px;height:42px">Property Address including City, State and Zip Code*</div>
    <div class="field" style="left:24px;top:240px;width:418px;height:42px">Repairs needed if any</div>
    <div class="field" style="left:24px;top:286px;width:418px;height:140px">Comments</div>
    <div class="submit-btn">Submit, To Get Started Selling Your Home Fast</div>
    <div class="privacy-note"><svg width="10" height="12" viewBox="0 0 10 12"><rect x="1" y="5" width="8" height="6" fill="#aab"/><path d="M3 5 V3 a2 2 0 0 1 4 0 V5" fill="none" stroke="#aab" stroke-width="1.4"/></svg>We guarantee 100% privacy.</div>
  </form>
</section>

<section>
  <div class="abs sell-band"></div>
  <h2 class="abs sell-title">SELL YOUR HOME OR HOUSE FAST FOR CASH TO A PROFESSIONAL INVESTOR COMPANY. WE BUY HOUSES AND CLOSE QUICKLY.</h2>
  <p class="abs sell-copy">Selling a home on your own has never been easier. From Orlando to Greensboro - and all points in between- you can sell your home today without any hassles. <strong>Call 1-800-555-0176</strong> or fill out the form Above to get a written offer on your home in just 36 hours. Sell today online to people that care.</p>
  <h3 class="abs reasons-title">If you need to sell a home fast because of:</h3>
  <ul class="abs reasons-list">
    <li><svg width="16" height="10" viewBox="0 0 16 10"><path d="M1 9 Q6 2 14 3 M10 0 L15 3 L11 7" fill="none" stroke="var(--red)" stroke-width="2"/></svg>Divorce or Bankruptcy</li>
    <li><svg width="16" height="10" viewBox="0 0 16 10"><path d="M1 9 Q6 2 14 3 M10 0 L15 3 L11 7" fill="none" stroke="var(--red)" stroke-width="2"/></svg>Foreclosure</li>
    <li><svg width="16" height="10" viewBox="0 0 16 10"><path d="M1 9 Q6 2 14 3 M10 0 L15 3 L11 7" fill="none" stroke="var(--red)" stroke-width="2"/></svg>Landlord problems - evictions with tenants okay</li>
    <li><svg width="16" height="10" viewBox="0 0 16 10"><path d="M1 9 Q6 2 14 3 M10 0 L15 3 L11 7" fill="none" stroke="var(--red)" stroke-width="2"/></svg>Inherited property in probate</li>
    <li><svg width="16" height="10" viewBox="0 0 16 10"><path d="M1 9 Q6 2 14 3 M10 0 L15 3 L11 7" fill="none" stroke="var(--red)" stroke-width="2"/></svg>Termites, mold, flood or fire damage, leaky roof</li>
    <li><svg width="16" height="10" viewBox="0 0 16 10"><path d="M1 9 Q6 2 14 3 M10 0 L15 3 L11 7" fill="none" stroke="var(--red)" stroke-width="2"/></svg>Moving or can't afford mortgage payments</li>
  </ul>
  <p class="abs help-line">We Can Help. We Are The Fastest Home Buyers Around.</p>

  <div class="abs privacy-btn">Our Privacy Policy</div>
  <div class="abs share-squares"><span></span><span class="mid"></span><span></span></div>
  <p class="abs call-hours">Call Us <em>8am To 10 Pm</em> Eastern Time.<br>We Answer Our Phones.</p>
  <h3 class="abs testimonials-title">HOME SELLER TESTIMONIALS</h3>
  <p class="abs testimonial-quote">I just wanted to thank you for buying my home in Winter Park. You made it fast and easy and kept me well informed the whole way.</p>
  <p class="abs testimonial-name">Dorsey Kettering – Winter Park</p>
  <div class="abs dots"><span></span><span class="on"></span><span></span><span></span></div>
  <div class="abs more-btn">More Testimonials</div>
</section>

<section>
  <div class="abs sidebar-bg"></div>

  <article>
    <div class="post-photo" style="top:1728px" role="img" aria-label="Photo of a white single-storey house with shrubs"></div>
    <h3 class="post-title active" style="top:1894px">BLOG ENTRY 1</h3>
    <div class="post-meta" style="top:1900px"><span><svg width="10" height="11" viewBox="0 0 10 11"><circle cx="5" cy="3" r="2.5" fill="#aaa"/><path d="M0 11 a5 5 0 0 1 10 0z" fill="#aaa"/></svg>by President Marlon</span><span><svg width="11" height="11" viewBox="0 0 11 11"><rect x=".5" y="1.5" width="10" height="9" fill="none" stroke="#aaa"/><rect x=".5" y="1.5" width="10" height="2.5" fill="#aaa"/></svg>June 10th, 2015</span></div>
    <p class="post-text" style="top:1928px">The US economy has failed to improve over recent months, and at the same time the Australian economy is slowing due to weakness in Asia. This begs the question of whether or not a Recession is just ar ... <i class="active">Continue Reading &gt;</i></p>
  </article>
  <article>
    <div class="post-photo" style="top:2042px" role="img" aria-label="Photo of a white single-storey house with shrubs"></div>
    <h3 class="post-title" style="top:2212px">BLOG ENTRY 2</h3>
    <div class="post-meta" style="top:2218px"><span><svg width="10" height="11" viewBox="0 0 10 11"><circle cx="5" cy="3" r="2.5" fill="#aaa"/><path d="M0 11 a5 5 0 0 1 10 0z" fill="#aaa"/></svg>by President Marlon</span><span><svg width="11" height="11" viewBox="0 0 11 11"><rect x=".5" y="1.5" width="10" height="9" fill="none" stroke="#aaa"/><rect x=".5" y="1.5" width="10" height="2.5" fill="#aaa"/></svg>June 10th, 2015</span></div>
    <p class="post-text" style="top:2246px">The US economy has failed to improve over recent months, and at the same time the Australian economy is slowing due to weakness in Asia. This begs the question of whether or not a Recession is just ar ... <i>Continue Reading &gt;</i></p>
  </article>
  <article>
    <div class="post-photo" style="top:2358px" role="img" aria-label="Photo of a white single-storey house with shrubs"></div>
    <h3 class="post-title" style="top:2528px">BLOG ENTRY 3</h3>
    <div class="post-meta" style="top:2534px"><span><svg width="10" height="11" viewBox="0 0 10 11"><circle cx="5" cy="3" r="2.5" fill="#aaa"/><path d="M0 11 a5 5 0 0 1 10 0z" fill="#aaa"/></svg>by President Marlon</span><span><svg width="11" height="11" viewBox="0 0 11 11"><rect x=".5" y="1.5" width="10" height="9" fill="none" stroke="#aaa"/><rect x=".5" y="1.5" width="10" height="2.5" fill="#aaa"/></svg>June 10th, 2015</span></div>
    <p class="post-text" style="top:2562px">The US economy has failed to improve over recent months, and at the same time the Australian economy is slowing due to weakness in Asia. This begs the question of whether or not a Recession is just ar ... <i>Continue Reading &gt;</i></p>
  </article>

  <ul class="abs archive-list">
    <li>Archives</li><li>Sell my house</li><li>Fast cash for homes</li><li>We buy houses</li><li>Real Estate investor</li><li>Latest</li>
  </ul>

  <aside>
    <div class="abs about-photo" role="img" aria-label="Portrait photo of the company owner"></div>
    <h3 class="abs about-title">ABOUT US</h3>
    <p class="abs about-copy">Owned and operated in Orlando Florida since 2001. Oldest Continuous operated website in country.</p>
    <div class="abs rule" style="top:1872px"></div>
    <h3 class="abs cities-title">SOME OF THE CITIES WHERE WE BUY HOUSES. NOT ALL ARE LISTED.</h3>
    <p class="abs cities-lead">These are the cities where we have an affiliate where you can sell a home fast or quickly and we buy homes:</p>
    <p class="abs cities-copy">Orlando Jacksonville Ft Myers Tampa St Pete Gainesville Tallahassee Melbourne West Palm Beach Apopka Deland Kissimmee Lakeland Ocala Chicago Philadelphia Camden <strong>Atlanta</strong> Valdosta Houston Detroit Phoenix Seattle Tacoma Portland Charlotte Cincinnati San Antonio Harrisburg Virginia Beach Virginia Homes Greensboro Charleston SC Flint Rochester Lake Florida Wilmington Columbia Titusville If you don't see your city, we still probably buy homes there.</p>
    <div class="abs rule" style="top:2216px"></div>
    <p class="abs types-lead">These are the types of real estate that we buy:</p>
    <p class="abs types-copy">We buy nice houses and outdated problem homes. We buy in great neighborhoods and not so nice. We buy block homes and frame homes.</p>
    <div class="abs rule" style="top:2336px"></div>
    <div class="abs houses-photo left" role="img" aria-label="Photo of a worn house with a concrete driveway and trees"></div>
    <div class="abs houses-photo right" role="img" aria-label="Photo of a tidy single-storey house with a green lawn"></div>
    <p class="abs houses-caption">We buy nice pretty houses and some ugly ones as well.</p>
  </aside>
</section>

<footer class="abs site-footer">
  <nav class="footer-nav"><span>SELL YOUR HOME</span><span>HOW IT WORKS</span><span>STOP FORECLOSURE</span><span>PROBATE</span><span>CONTACT</span></nav>
  <p class="copyright">© Copyright 2015 . All Rights Reserved.</p>
</footer>

</body>
</html>
```